SilverLedgerOak - Double Sided Business Card

We are looking for design options or our business cards. We are a Business Solutions and HR solutions Provider - the theme is business, for this card.

Our brand colours are represented within our logo.

Details needed to be put on the front of the business card are:

Employees name: [Sample Name]
Role: [Sample Role]

Address: Suite 4 - Level 3/48 Halloran Avenue Parramatta NSW 2150
M: 0000 000 000
P: 1300 847 213
F: 1300 847 286
E: sample@silverledgeroak.com.au
www.silverledgeroak.com.au
Updates

Reason: Hello, could we please increase our deadline by 5 days. Thanking you, Tess

Target Market(s)

Business Owners, also Candidates looking for Employment

Industry/Entity Type

Business

Contact Information for Business Card

Role: [Sample Role]

M: 0000 000 000
P: 1300 847 213
F: 1300 847 286

Font styles to use
Sans Serif

Colors
3276b5
3176b5
0455a3
85abd2
cfdeed
ffffff
000000
1b1b1b
757575

Requirements
Must have
• Details needed to be put on the front of the business card are:
• Employees name: [Sample Name]
• Role: [Sample Role]
• Address: Suite 4 - Level 3/48 Halloran Avenue Parramatta NSW 2150
• M: 0000 000 000
• P: 1300 847 213
• F: 1300 847 286
• E: sample@silverledgeroak.com.au
• www.silverledgeroak.com.au
Nice to have
• Simplicity, clean and professional.

```html
<!DOCTYPE html>
<html lang="en">
<head>
<meta charset="utf-8">
<title>SilverLedgerOak – Business Card</title>
<link href="https://fonts.googleapis.com/css2?family=Open+Sans:wght@400;600;700;800&display=swap" rel="stylesheet">
<style>
  :root {
    --page-bg: #ecebea;
    --card-white: #ffffff;
    --steel-blue: #1b7bb0;
    --navy: #122a46;
    --royal-blue: #0d57a6;
    --sky-blue: #2fb0e4;
    --panel-dark: #38393a;
    --row-grey: #4a4c4e;
    --ink: #000000;
  }
  html, body {
    margin: 0;
    padding: 0;
    width: 1200px;
    height: 1200px;
    overflow: hidden;
    background: var(--page-bg);
  }
  .canvas {
    position: relative;
    width: 1200px;
    height: 1200px;
  }
  .card {
    position: absolute;
    display: block;
    box-shadow: 0 10px 24px rgba(0,0,0,0.18);
  }
  .card--front { left: 208px; top: 118px; width: 780px; height: 445px; }
  .card--back  { left: 209px; top: 635px; width: 772px; height: 441px; }

  .fill-white { fill: var(--card-white); }
  .fill-steel { fill: var(--steel-blue); }
  .fill-navy { fill: var(--navy); }
  .fill-royal { fill: var(--royal-blue); }
  .fill-sky { fill: var(--sky-blue); }
  .fill-panel { fill: var(--panel-dark); }
  .fill-row { fill: var(--row-grey); }

  .icon-hex { fill: var(--sky-blue); stroke: #ffffff; stroke-width: 2; }
  .icon-glyph { fill: #ffffff; }
  .icon-line { fill: none; stroke: #ffffff; stroke-width: 2; }

  .brand-name {
    font-family: "Open Sans", sans-serif;
    font-weight: 700;
    fill: var(--royal-blue);
  }
  .staff-name {
    font-family: "Open Sans", sans-serif;
    font-weight: 800;
    font-size: 34px;
    fill: #ffffff;
  }
  .staff-role {
    font-family: "Open Sans", sans-serif;
    font-weight: 400;
    font-size: 17px;
    fill: #ffffff;
  }
  .contact-text {
    font-family: "Open Sans", sans-serif;
    font-weight: 400;
    font-size: 23px;
    fill: #ffffff;
  }
  .address-text {
    font-family: "Open Sans", sans-serif;
    font-weight: 400;
    font-size: 19px;
    fill: #ffffff;
  }
  .web-text {
    font-family: "Open Sans", sans-serif;
    font-weight: 400;
    font-size: 23px;
    fill: #ffffff;
  }
  .tagline {
    font-family: "Open Sans", sans-serif;
    font-weight: 700;
    font-size: 14px;
    fill: var(--ink);
  }
</style>
</head>
<body>
<div class="canvas">

  <!-- Front of card -->
  <svg class="card card--front" viewBox="0 0 780 445" xmlns="http://www.w3.org/2000/svg">
    <defs>
      <clipPath id="panel-clip">
        <path d="M352,0 C300,120 290,300 362,445 L780,445 L780,0 Z"/>
      </clipPath>
    </defs>

    <rect class="fill-white" x="0" y="0" width="780" height="445"/>

    <!-- edge stripe -->
    <rect class="fill-steel" x="0" y="0" width="24" height="222"/>
    <rect class="fill-navy" x="0" y="222" width="24" height="223"/>

    <!-- curved accent and dark panel -->
    <path class="fill-sky" d="M336,0 C282,120 272,300 346,445 L362,445 C290,300 300,120 352,0 Z"/>
    <path class="fill-panel" d="M352,0 C300,120 290,300 362,445 L780,445 L780,0 Z"/>

    <!-- contact rows -->
    <g clip-path="url(#panel-clip)">
      <rect class="fill-row" x="300" y="119" width="480" height="46"/>
      <rect class="fill-row" x="300" y="180" width="480" height="46"/>
      <rect class="fill-row" x="300" y="241" width="480" height="46"/>
      <rect class="fill-row" x="300" y="301" width="480" height="46"/>
      <rect class="fill-row" x="300" y="362" width="480" height="46"/>
    </g>

    <!-- name band with fold -->
    <polygon class="fill-steel" points="298,103 330,103 330,60"/>
    <rect class="fill-sky" x="316" y="39" width="464" height="64"/>
    <polygon class="fill-sky" points="298,103 316,39 330,39 330,103"/>

    <!-- icons -->
    <g class="icon icon--person" transform="translate(375,68)">
      <polygon class="icon-hex" points="-11,-19 11,-19 22,0 11,19 -11,19 -22,0"/>
      <circle class="icon-glyph" cx="0" cy="-4" r="4"/>
      <path class="icon-glyph" d="M-7,7 Q0,-2 7,7 Z"/>
    </g>
    <g class="icon icon--mobile" transform="translate(353,141)">
      <polygon class="icon-hex" points="-11,-19 11,-19 22,0 11,19 -11,19 -22,0"/>
      <rect class="icon-line" x="-5" y="-9" width="10" height="18" rx="2"/>
    </g>
    <g class="icon icon--phone" transform="translate(345,202)">
      <polygon class="icon-hex" points="-11,-19 11,-19 22,0 11,19 -11,19 -22,0"/>
      <path class="icon-glyph" d="M-8,-8 L-4,-9 L-1,-3 L-4,-1 Q-2,3 2,5 L4,2 L9,5 L8,9 Q-7,9 -8,-8 Z"/>
    </g>
    <g class="icon icon--fax" transform="translate(348,262)">
      <polygon class="icon-hex" points="-11,-19 11,-19 22,0 11,19 -11,19 -22,0"/>
      <rect class="icon-glyph" x="-5" y="-9" width="10" height="5"/>
      <rect class="icon-glyph" x="-9" y="-3" width="18" height="8" rx="1"/>
      <rect class="icon-glyph" x="-5" y="6" width="10" height="4"/>
    </g>
    <g class="icon icon--mail" transform="translate(357,320)">
      <polygon class="icon-hex" points="-11,-19 11,-19 22,0 11,19 -11,19 -22,0"/>
      <rect class="icon-glyph" x="-8" y="-6" width="16" height="12"/>
      <path d="M-8,-6 L0,1 L8,-6" fill="none" stroke="var(--sky-blue)" stroke-width="1.5"/>
    </g>
    <g class="icon icon--pin" transform="translate(379,382)">
      <polygon class="icon-hex" points="-11,-19 11,-19 22,0 11,19 -11,19 -22,0"/>
      <path class="icon-glyph" d="M0,9 L-6,-1 A7,7 0 1 1 6,-1 Z"/>
      <circle cx="0" cy="-4" r="2.5" fill="var(--sky-blue)"/>
    </g>

    <!-- name and role -->
    <text class="staff-name" x="427" y="72">DANIEL</text>
    <text class="staff-role" x="427" y="96">ASSISTANT DIRECTOR</text>

    <!-- contact details -->
    <text class="contact-text" x="413" y="150">0000 000 000</text>
    <text class="contact-text" x="413" y="211">1300 847 213</text>
    <text class="contact-text" x="413" y="270">1300 847 286</text>
    <text class="contact-text" x="413" y="330">sample@silverledgeroak.com.au</text>
    <text class="address-text" x="411" y="383">Suite 4 - Level 3/48 Halloran Avenue</text>
    <text class="address-text" x="411" y="403">Parramatta NSW 2150</text>

    <!-- website bar -->
    <rect class="fill-royal" x="108" y="418" width="564" height="27"/>
    <text class="web-text" x="390" y="441" text-anchor="middle">www.silverledgeroak.com.au</text>

    <!-- brand name -->
    <text class="brand-name" x="157" y="266" font-size="24" text-anchor="middle">SilverLedgerOak</text>
  </svg>

  <!-- Back of card -->
  <svg class="card card--back" viewBox="0 0 772 441" xmlns="http://www.w3.org/2000/svg">
    <rect class="fill-white" x="0" y="0" width="772" height="441"/>

    <rect class="fill-steel" x="0" y="0" width="386" height="45"/>
    <rect class="fill-navy" x="386" y="0" width="386" height="45"/>

    <rect class="fill-navy" x="0" y="396" width="386" height="45"/>
    <rect class="fill-steel" x="386" y="396" width="386" height="45"/>

    <text class="brand-name" x="386" y="280" font-size="52" text-anchor="middle">SilverLedgerOak</text>
    <text class="tagline" x="386" y="343" text-anchor="middle">Helping small to medium business realise their potential</text>
  </svg>

</div>
</body>
</html>
```